Visitenkarten-Design für Stillberaterin
Zielgruppe
Ich bin Stillberaterin ZMRPT, d. h. ich berate Mütter bei Stillschwierigkeiten. Meine Zielgruppe sind junge Familien, die sich vorab über das Stillen Ihres Kindes informieren möchten, Stillschwierigkeiten (z. B. Schmerzen, schlechte Gewichtszunahme usw.) haben oder Fragen rund ums Stillen haben (Medikamente, Stillen in besonderen Situationen...). Weiterhin biete ich Kurse für den Beikoststart oder zum Abstillen an.
Aufgabenstellung
Auf meiner Visitenkarte sollte mein Logo sowie alle Kontaktdaten klar und deutlich erkennbar sein. Die Farben sind dem Logo anzupassen. Die Schriftarten, die im Logo verwendet werden sind: Be Bright und Apple Tree

```html
<!DOCTYPE html>
<html lang="de">
<head>
<meta charset="utf-8">
<title>Visitenkarte Stillberatung</title>
<link href="https://fonts.googleapis.com/css2?family=Andika&family=Carlito&family=Dancing+Script:wght@500&display=swap" rel="stylesheet">
<style>
  :root {
    --stage: #333333;
    --paper: #ffffff;
    --pink: #ee5aa1;
    --pink-light: #f7c6dd;
    --grey-script: #6f6f6f;
    --ink: #222222;
  }
  * { margin: 0; padding: 0; box-sizing: border-box; }
  html, body { width: 1073px; height: 1200px; overflow: hidden; background: var(--stage); }
  .canvas { position: relative; width: 1073px; height: 1200px; }
  .card { position: absolute; left: 175px; width: 723px; height: 460px; }
  .card--front { top: 101px; background: var(--paper); }
  .card--back { top: 623px; background: var(--pink); }

  .frame { position: absolute; left: 28px; top: 33px; width: 664px; height: 399px; border: 1.5px solid var(--pink); border-radius: 14px; }
  .corner { position: absolute; width: 58px; height: 58px; background: radial-gradient(circle, rgba(238,90,161,0.18), rgba(238,90,161,0.05)); border-radius: 6px; }
  .corner--tl { left: 28px; top: 33px; }
  .corner--tr { left: 634px; top: 33px; }
  .corner--bl { left: 28px; top: 374px; }
  .corner--br { left: 634px; top: 374px; }

  .brand-mark { position: absolute; left: 100px; top: 200px; width: 160px; text-align: center; }
  .brand-mark__dot { display: block; width: 54px; height: 54px; margin: 0 auto 10px; border: 2px solid var(--pink); border-radius: 50%; }
  .brand-mark__name { font-family: "Andika", sans-serif; font-size: 22px; color: var(--pink); }

  .person-name { position: absolute; left: 304px; top: 88px; font-family: "Dancing Script", cursive; font-weight: 500; font-size: 52px; color: var(--grey-script); line-height: 1; }
  .person-role { position: absolute; left: 310px; top: 164px; font-family: "Andika", sans-serif; font-size: 16.5px; line-height: 26px; color: var(--ink); }
  .address { position: absolute; left: 310px; top: 244px; font-family: "Carlito", sans-serif; font-size: 21.5px; line-height: 30px; color: var(--ink); }
  .contact { position: absolute; left: 311px; top: 321px; font-family: "Carlito", sans-serif; font-size: 21.5px; line-height: 30px; color: var(--ink); list-style: none; }
  .contact li { display: flex; align-items: center; }
  .contact svg { width: 20px; height: 16px; margin-right: 12px; fill: var(--pink); }

  .back-mark { position: absolute; left: 311px; top: 110px; width: 100px; height: 100px; border: 2px solid var(--pink-light); border-radius: 50%; }
  .back-name { position: absolute; left: 0; top: 240px; width: 100%; text-align: center; font-family: "Andika", sans-serif; font-size: 52px; color: var(--pink-light); line-height: 1; }
  .back-tagline { position: absolute; left: 0; top: 318px; width: 100%; text-align: center; font-family: "Andika", sans-serif; font-size: 17px; color: var(--pink-light); }
  .back-web { position: absolute; left: 0; top: 406px; width: 100%; text-align: center; font-family: "Dancing Script", cursive; font-size: 26px; color: var(--pink-light); line-height: 1; }
  .flourish { position: absolute; top: 414px; width: 84px; height: 14px; background: linear-gradient(90deg, rgba(247,198,221,0.1), rgba(247,198,221,0.45), rgba(247,198,221,0.1)); border-radius: 7px; }
  .flourish--left { left: 136px; }
  .flourish--right { left: 509px; }
</style>
</head>
<body>
<div class="canvas">
  <section class="card card--front">
    <div class="frame"></div>
    <div class="corner corner--tl" role="img" aria-label="Rankenornament in der Ecke"></div>
    <div class="corner corner--tr" role="img" aria-label="Rankenornament in der Ecke"></div>
    <div class="corner corner--bl" role="img" aria-label="Rankenornament in der Ecke"></div>
    <div class="corner corner--br" role="img" aria-label="Rankenornament in der Ecke"></div>

    <div class="brand-mark">
      <span class="brand-mark__dot"></span>
      <span class="brand-mark__name">Stillzeit-Nah</span>
    </div>

    <h1 class="person-name">Marlene Vogt</h1>
    <p class="person-role">Fachkinderkrankenschwester,<br>Still- &amp; Laktationsberaterin ZMRPT</p>
    <p class="address">Am Lindenhang 4<br>93099 Wiesenau</p>
    <ul class="contact">
      <li><svg viewBox="0 0 24 24" aria-hidden="true"><path d="M6.6 10.8c1.4 2.8 3.8 5.1 6.6 6.6l2.2-2.2c.3-.3.7-.4 1-.2 1.1.4 2.3.6 3.6.6.6 0 1 .4 1 1V20c0 .6-.4 1-1 1C10.6 21 3 13.4 3 4c0-.6.4-1 1-1h3.5c.6 0 1 .4 1 1 0 1.3.2 2.5.6 3.6.1.3 0 .7-.2 1l-2.3 2.2z"/></svg>09401 7281905</li>
      <li><svg viewBox="0 0 24 18" aria-hidden="true"><path d="M0 0h24v18H0z M2 2l10 8 10-8" fill="var(--pink)"/><path d="M1 1l11 9 11-9" fill="none" stroke="#fff" stroke-width="1.6"/></svg>marlene@stillzeit-nah.de</li>
    </ul>
  </section>

  <section class="card card--back">
    <span class="back-mark"></span>
    <p class="back-name">Stillzeit-Nah</p>
    <p class="back-tagline">Stillberatung für Regensburg</p>
    <div class="flourish flourish--left" role="img" aria-label="Schnörkelornament"></div>
    <p class="back-web">www.stillzeit-nah.de</p>
    <div class="flourish flourish--right" role="img" aria-label="Schnörkelornament"></div>
  </section>
</div>
</body>
</html>
```